Real Estate Marketing Company Needs 1 Page 8.5x11 Price List Flyer Design

We need a 1 page 8.5in x 11in price list flyer that is intended for drop off at local offices. This is intended to show all the services we offer including pricing to potential new clients. It should be separated into sections for the different services we offer. I'd also like some photos and our Logo on the list to make it look nice so its not all text. Try to incorporate the logo colors in the design.

Industry/Entity Type

Real Estate

Requirements
Must have
• Price List
• Photos
• Logo
• website address

```html
<!DOCTYPE html>
<html lang="en">
<head>
<meta charset="utf-8">
<title>Keystone Lens Photography – Price List Flyer</title>
<link rel="stylesheet" href="https://fonts.googleapis.com/css2?family=League+Gothic&family=Open+Sans:wght@400;600;700&family=Cinzel:wght@500&display=swap">
<style>
:root{
  --backdrop:#8a8a8a;
  --sage:#a8b8a2;
  --charcoal:#3d3532;
  --white:#ffffff;
  --ink:#2a2a2a;
  --foliage:#4f6f3c;
  --sky:#8fa8b8;
  --pool:#4f94c4;
  --interior:#b9a58a;
  --twilight:#8c6f9a;
  --brick:#7a5548;
  --porch:#6f8a55;
  --aerial:#4e6b3a;
  --plan:#f1f0ec;
}
*{margin:0;padding:0;box-sizing:border-box}
html,body{width:1200px;height:802px;overflow:hidden}
body{background:var(--backdrop);position:relative;font-family:"Open Sans",Arial,sans-serif;color:var(--ink)}
.page{position:absolute;top:70px;width:515px;height:661px;overflow:hidden;background:var(--white)}
.page--front{left:70px}
.page--back{left:615px}
.front-art{position:absolute;inset:0}
.headline{position:absolute;left:152px;top:58px;width:316px;text-align:center;font-family:"League Gothic","Oswald",Arial Narrow,sans-serif;font-weight:400;font-size:38px;line-height:1;color:var(--white);letter-spacing:.3px;white-space:nowrap}
.brand{position:absolute;left:30px;top:238px;width:204px;text-align:center;font-family:"Cinzel",Georgia,serif;font-weight:500;color:var(--ink)}
.brand__mark{width:72px;height:72px;border-radius:50%;background:var(--ink);margin:0 auto 12px}
.brand__name{font-size:24px;line-height:1.05;white-space:nowrap}
.brand__sub{font-size:10px;letter-spacing:6px;margin-top:5px}

.band{position:absolute;left:0;width:515px}
.band--pricing{top:0;height:162px;background:var(--sage)}
.band--photo-only{top:162px;height:58px;background:var(--charcoal);color:var(--white);padding:13px 0 0 53px}
.band--extras{top:220px;height:188px;background:var(--sage)}
.band--plans{top:408px;height:142px;background:var(--white)}
.band--contact{top:550px;height:111px;background:var(--charcoal)}
.section-title{font-weight:700;font-size:13.5px;letter-spacing:.2px;color:var(--ink)}
.band--photo-only .section-title{color:var(--white)}
.pricing{padding:50px 0 0 53px}
.tiers{display:flex;margin-top:9px}
.tier{font-size:10.5px;line-height:1.35;color:var(--ink)}
.tier--silver{width:121px}
.tier--gold{width:142px}
.tier--gold,.tier--platinum{border-left:1px dashed #6e776a;padding-left:20px}
.tier--platinum{width:150px}
.tier h3{font-size:11.5px;font-weight:600}
.tier strong{display:block;font-size:13px;margin-top:2px}
.bundles{font-size:9px;margin-top:2px}
.bundles b{font-weight:700}
.bundles span{margin:0 8px}
.photo{position:absolute}
.photo--interior{left:0;top:220px;width:292px;height:188px;background:linear-gradient(160deg,#e6dccb,var(--interior) 55%,#6f5e4c)}
.extras{position:absolute;left:319px;top:237px;width:192px}
.extras p{font-size:9px;line-height:1.32;margin-top:9px}
.extras p small{font-size:7px;display:block}
.photo--plan{left:37px;top:414px;width:173px;height:247px;background:var(--plan);border:1px solid #dcdad4}
.plans{position:absolute;left:244px;top:442px}
.plans p{font-size:8.6px;margin-top:7px}
.plans .note{font-size:7px;margin-top:8px;line-height:1.35}
.contact{position:absolute;left:245px;top:576px;color:#e9e6e2;font-size:10px;line-height:1.4}
.contact b{color:var(--white)}
</style>
</head>
<body>

<section class="page page--front">
  <svg class="front-art" width="515" height="661" viewBox="0 0 515 661">
    <rect width="515" height="661" fill="var(--sage)"/>
    <polygon points="0,0 515,0 515,330 270,330 0,48" fill="url(#poolGrad)" role="img" aria-label="Photo of a backyard pool with a white pool house surrounded by trees"/>
    <polygon points="0,48 270,330 0,612" fill="var(--white)"/>
    <polygon points="515,345 515,661 180,661" fill="url(#aerialGrad)" role="img" aria-label="Aerial photo of a large house surrounded by woodland"/>
    <circle cx="323" cy="335" r="72" fill="var(--white)"/>
    <circle cx="323" cy="335" r="63" fill="url(#porchGrad)" role="img" aria-label="Photo of a covered porch with wicker chairs and cushions"/>
    <circle cx="173" cy="490" r="92" fill="var(--white)"/>
    <circle cx="173" cy="490" r="83" fill="url(#twilightGrad)" role="img" aria-label="Twilight photo of a brick house in snow"/>
    <defs>
      <linearGradient id="poolGrad" x1="0" y1="0" x2="0" y2="1">
        <stop offset="0" stop-color="var(--sky)"/><stop offset=".35" stop-color="var(--foliage)"/><stop offset=".75" stop-color="var(--pool)"/><stop offset="1" stop-color="#6b8a52"/>
      </linearGradient>
      <linearGradient id="aerialGrad" x1="0" y1="0" x2="1" y2="1">
        <stop offset="0" stop-color="#7d9a6a"/><stop offset=".6" stop-color="var(--aerial)"/><stop offset="1" stop-color="#3d5a2e"/>
      </linearGradient>
      <linearGradient id="porchGrad" x1="0" y1="0" x2="0" y2="1">
        <stop offset="0" stop-color="var(--porch)"/><stop offset=".6" stop-color="#c9c2b2"/><stop offset="1" stop-color="#8a7258"/>
      </linearGradient>
      <linearGradient id="twilightGrad" x1="0" y1="0" x2="0" y2="1">
        <stop offset="0" stop-color="var(--twilight)"/><stop offset=".55" stop-color="var(--brick)"/><stop offset="1" stop-color="#e6e8f0"/>
      </linearGradient>
    </defs>
  </svg>
  <h1 class="headline">PRESENTATION IS EVERYTHING</h1>
  <div class="brand">
    <div class="brand__mark"></div>
    <div class="brand__name">KEYSTONE LENS</div>
    <div class="brand__sub">PHOTOGRAPHY</div>
  </div>
</section>

<section class="page page--back">
  <div class="band band--pricing">
    <div class="pricing">
      <h2 class="section-title">PACKAGE PRICING:</h2>
      <div class="tiers">
        <div class="tier tier--silver"><h3>Silver Package:</h3>15 Photos +<br>Floor Plan (3,500 sqft)<strong>$225</strong></div>
        <div class="tier tier--gold"><h3>Gold Package:</h3>25 Photos +<br>Floor Plan (4,500 sqft)<strong>$300</strong></div>
        <div class="tier tier--platinum"><h3>Platinum Package:</h3>35 Photos +<br>Floor Plan (5,500 sqft)<strong>$375</strong></div>
      </div>
    </div>
  </div>

  <div class="band band--photo-only">
    <h2 class="section-title">PHOTOGRAPHY ONLY</h2>
    <p class="bundles">15 Photo Bundle : <b>$100</b><span>|</span>25 Photo Bundle : <b>$150</b><span>|</span>35 Photo Bundle : <b>$200</b></p>
  </div>

  <div class="band band--extras"></div>
  <div class="photo photo--interior" role="img" aria-label="Photo of a bright living room with vaulted ceiling and lanterns"></div>
  <div class="extras">
    <h2 class="section-title">ADDITIONAL SERVICES</h2>
    <p>Aerial Photos: 3-6 Photos - <b>$200</b><small>($75 if combined with another package)</small></p>
    <p>Aerial Video: (1-3 min video) - <b>$375</b></p>
    <p>Branded Video Tour w/ Aerial Video:<br>(2-4 min video of property) - <b>$800-$1300</b><small>(voiceover optional, call for details)</small></p>
    <p>Twilight Photos: 3-6 Photos - <b>$225</b><br>Luxury Package: <b>$2,000</b><small>(includes all services listed)</small></p>
  </div>

  <div class="band band--plans"></div>
  <div class="band band--contact"></div>
  <div class="photo photo--plan" role="img" aria-label="Two-storey floor plan drawing with labelled rooms"></div>
  <div class="plans">
    <h2 class="section-title">FLOOR PLANS</h2>
    <p>Floor Plan (3,500 sqft) - <b>$150</b></p>
    <p>Floor Plan (4,500 sqft) - <b>$175</b></p>
    <p>Floor Plan (5,500 sqft) - <b>$200</b></p>
    <p class="note">*$25 per additional 500sqft<br>**Complex floor plans are priced individually regardless of sqft</p>
  </div>
  <p class="contact">For more information or to book<br>a shoot please visit our website:<br><b>www.KeystoneLensPhoto.com</b> or<br>call Dana at <b>555-014-2287</b></p>
</section>

</body>
</html>
```